Gummy Label design for hemp company

I need a 3.25 inch wide by 4 inch tall label made to be put on bags of gummies. I will include all disclaimers that need to be there, as well as my logo. This is for our 25 mg Delta 8 gummies 20ct, but I will use the design for our entire gummy line, just editing the text. Needs to have ingredient list. Ingredients: Sugar, Inulin, Corn syrup, water, pectin, citric acid, baking soda, fruit, hemp extract.

Everything should be on one label as this is going on a sticker that will be placed on a bag.
I would like to highlight that they are vegan if possible.

• Must have the following disclaimer: "Contains Farm Bill compliant hemp extract. These statements have not been evaluated by the QVR. This product is NOT intended to treat, cure, or prevent any disease. Do not operate heavy machinery while using this product. This product may cause you to fail a drug test. Consult with your doctor before trying any new products. Do not take if pregnant or lactating. If you experience any adverse effects, discontinue use and seek advice from your physician."
• NEEDS TO SAY: "100% hemp derived" also "<.3% D9 THC"

```html
<!DOCTYPE html>
<html lang="en">
<head>
<meta charset="utf-8">
<title>Delta 8 Gummies Label</title>
<link href="https://fonts.googleapis.com/css2?family=Rubik:wght@900&family=Montserrat:wght@400;500;600&family=Hind:wght@400;500&display=swap" rel="stylesheet">
<style>
  :root {
    --stage: #b1b3b1;
    --paper: #f7f7f6;
    --art-light: #f1f2f1;
    --art-dark: #dcdedc;
    --brand-green: #3d7d35;
    --title-outline: #3b7a33;
    --title-fill: #f3f5f3;
    --strip-green: #a0c23e;
    --badge-line: #6f6f6f;
    --badge-text: #5e5e5e;
    --icon-grey: #8a8a8a;
    --white: #ffffff;
  }
  * { margin: 0; padding: 0; box-sizing: border-box; }
  html, body { width: 1200px; height: 1200px; overflow: hidden; }
  body { background: var(--stage); position: relative; font-family: "Montserrat", sans-serif; }

  .label {
    position: absolute; left: 250px; top: 168px;
    width: 702px; height: 864px;
    display: flex;
  }
  .label-front {
    position: relative; width: 554px; height: 100%;
    background: var(--paper);
    overflow: hidden;
  }
  .background-art {
    position: absolute; inset: 0;
    background: radial-gradient(ellipse at 50% 55%, var(--art-dark) 0%, var(--art-light) 55%, var(--paper) 100%);
    opacity: 0.85;
  }
  .brand {
    position: absolute; left: 0; right: 0; top: 78px;
    display: flex; flex-direction: column; align-items: center; gap: 10px;
  }
  .brand-dot { width: 46px; height: 46px; border-radius: 50%; background: var(--brand-green); }
  .brand-name {
    font-family: "Montserrat", sans-serif; font-weight: 600;
    font-size: 32px; color: var(--brand-green); letter-spacing: 0.5px;
  }
  .product-title { position: absolute; left: 0; top: 0; width: 554px; height: 864px; }
  .product-title text {
    font-family: "Rubik", sans-serif; font-weight: 900; text-anchor: middle;
  }
  .title-outline { fill: var(--title-outline); stroke: var(--title-outline); stroke-width: 26; stroke-linejoin: round; }
  .title-fill { fill: var(--title-fill); stroke: #6da45f; stroke-width: 2; }

  .badges { position: absolute; left: 68px; top: 570px; width: 428px; }
  .badge {
    position: relative; height: 30px; margin-bottom: 16px;
    border: 2.5px solid var(--badge-line); background: var(--paper);
    display: flex; align-items: center; justify-content: center;
    font-size: 17px; letter-spacing: 4px; color: var(--badge-text); font-weight: 500;
  }
  .badge-icon {
    position: absolute; top: 50%; width: 38px; height: 38px; margin-top: -19px;
    border-radius: 50%; background: var(--icon-grey);
    display: flex; align-items: center; justify-content: center;
  }
  .badge-icon.left { left: -4px; }
  .badge-icon.right { right: 8px; }
  .badge-icon .icon-text { font-family: "Rubik", sans-serif; font-weight: 900; font-size: 12px; color: var(--white); letter-spacing: 0; }

  .serving {
    position: absolute; left: 0; right: 0; top: 764px; text-align: center;
    font-size: 23px; font-weight: 500; color: #666; letter-spacing: 0.5px;
  }

  .info-strip { position: relative; width: 148px; height: 100%; background: var(--strip-green); overflow: hidden; }
  .info-text {
    position: absolute; width: 852px; height: 140px;
    left: 50%; top: 50%;
    transform: translate(-50%, -50%) rotate(-90deg);
    color: var(--white); font-family: "Hind", sans-serif;
    display: flex; flex-direction: column; justify-content: center;
  }
  .ingredients { font-size: 17.5px; font-weight: 500; line-height: 1.2; margin-bottom: 2px; }
  .disclaimer { font-size: 13.6px; line-height: 1.38; }
</style>
</head>
<body>
  <main class="label">
    <section class="label-front">
      <div class="background-art" role="img" aria-label="Faint grey graffiti-style illustration of cartoon characters filling the label background"></div>

      <div class="brand">
        <span class="brand-dot"></span>
        <span class="brand-name">JoyLeaf Hemp</span>
      </div>

      <svg class="product-title" viewBox="0 0 554 864" aria-label="Delta 8 Gummies">
        <text class="title-outline" x="291" y="366" font-size="100" textLength="430" lengthAdjust="spacingAndGlyphs">DELTA 8</text>
        <text class="title-outline" x="280" y="462" font-size="100" textLength="423" lengthAdjust="spacingAndGlyphs">GUMMIES</text>
        <text class="title-fill" x="291" y="366" font-size="100" textLength="430" lengthAdjust="spacingAndGlyphs">DELTA 8</text>
        <text class="title-fill" x="280" y="462" font-size="100" textLength="423" lengthAdjust="spacingAndGlyphs">GUMMIES</text>
      </svg>

      <div class="badges">
        <div class="badge">
          <span class="badge-icon left">
            <svg width="22" height="22" viewBox="0 0 22 22"><path d="M4 18 C4 8 10 4 19 4 C19 13 14 18 4 18 Z M4 18 L13 10" fill="#fff" stroke="#8a8a8a" stroke-width="1.5"/></svg>
          </span>
          VEGAN
        </div>
        <div class="badge">
          100% HEMP DERIVED
          <span class="badge-icon right"></span>
        </div>
        <div class="badge">
          <span class="badge-icon left"><span class="icon-text">THC</span></span>
          &lt;.3% D9 THC
        </div>
      </div>

      <p class="serving">25MG PER GUMMY | 20 COUNT</p>
    </section>

    <aside class="info-strip">
      <div class="info-text">
        <p class="ingredients">Ingredients: Sugar, Inulin, Corn syrup, water, pectin, citric acid, baking soda, fruit, hemp extract.</p>
        <p class="disclaimer">Contains Farm Bill compliant hemp extract. These statements have not been evaluated by the QVR. This product is NOT intended to treat, cure, or prevent any disease. Do not operate heavy machinery while using this product. This product may cause you to fail a drug test. Consult with your doctor before trying any new products. Do not take if pregnant or lactating. If you experience any adverse effects, discontinue use and seek advice from your physician.</p>
      </div>
    </aside>
  </main>
</body>
</html>
```